Business Card and Stationary Design

After the successful redesign of our logo we are wanting to follow suite and create a new business card and stationary design!

New Logo is attached, information required on the business card should contain a mixture of the following but layout/arrangement is up to the designer.

Happy if the national provider number and abn are on the back, and happy for them to be smaller than the rest.

I am also happy to receive single sided or weird and wonderful designs.

Name
Title
National Provider Number 7291
ABN 53 219 864 317
Level 3, 42 Marlow Street
Ashby Heights NSW 2318
Ph: 1300 987 214
Mobile: 0432 785 619
name@ferngatebuild.com.au
www.ferngatebuild.com.au

Target Market(s)

Professionals, Peers, Students, Suppliers...

Industry/Entity Type

Construction

Contact Information for Business Card

Listed in project description

Font styles to use
Other font styles liked:
• Century Gothic

Colors
0455a3
3176b5
ffffff

Requirements
Must have
• Professional Design, same color scheme as our logo
Nice to have
• Something that sets our apart from everyone else would be fantastic, open to size and shape and layout options, as long as they present professionally.
• Open to raised/embossed text, alternative materials, custom sizes, clear material
Should not have
• The color orange

```html
<!DOCTYPE html>
<html lang="en">
<head>
<meta charset="utf-8">
<title>Ferngate Build – Business Card</title>
<link href="https://fonts.googleapis.com/css2?family=Arimo:wght@400;700&family=Questrial&display=swap" rel="stylesheet">
<style>
  :root {
    --brand-blue: #1f3a7a;
    --panel-grey: #7f7f7f;
    --text-grey: #6d6d6d;
    --card-white: #ffffff;
    --backdrop: #e9e6e1;
  }
  html, body {
    margin: 0;
    width: 1200px;
    height: 758px;
    overflow: hidden;
    background: var(--backdrop);
  }
  .stage {
    position: relative;
    width: 1200px;
    height: 758px;
  }
  .card {
    position: absolute;
    top: 224px;
    width: 540px;
    height: 310px;
    background: var(--card-white);
    box-shadow: 0 2px 6px rgba(0,0,0,.18);
    overflow: hidden;
    font-family: "Arimo", Arial, sans-serif;
  }
  .card--front { left: 40px; }
  .card--back { left: 620px; }

  /* front: decorative brand area */
  .brand-panel {
    position: absolute;
    left: 0;
    top: 0;
    width: 262px;
    height: 278px;
    background: linear-gradient(90deg, var(--brand-blue) 0%, var(--brand-blue) 55%, var(--panel-grey) 100%);
  }

  .details {
    position: absolute;
    left: 286px;
    top: 22px;
    right: 14px;
    color: var(--text-grey);
  }
  .person-name {
    margin: 0;
    font-weight: 700;
    font-size: 19px;
    letter-spacing: .3px;
    color: var(--brand-blue);
    text-transform: uppercase;
  }
  .person-title {
    margin: 2px 0 18px;
    font-size: 14px;
  }
  .contact-list {
    list-style: none;
    margin: 0 0 18px;
    padding: 0;
    font-size: 14px;
    line-height: 23px;
  }
  .contact-list li { display: flex; align-items: center; gap: 9px; }
  .contact-list svg { width: 13px; height: 13px; flex: none; fill: var(--brand-blue); }
  .address { margin: 0; font-size: 14.5px; line-height: 21px; }

  /* back */
  .brand {
    position: absolute;
    left: 0; right: 0;
    top: 78px;
    display: flex;
    justify-content: center;
    align-items: center;
    gap: 12px;
  }
  .brand-mark { width: 26px; height: 26px; background: var(--brand-blue); }
  .brand-name {
    font-family: "Questrial", "Century Gothic", sans-serif;
    font-size: 36px;
    color: var(--brand-blue);
  }
  .registration {
    position: absolute;
    left: 70px;
    top: 176px;
    margin: 0;
    font-size: 13px;
    line-height: 21px;
    color: var(--text-grey);
  }
</style>
</head>
<body>
<main class="stage">
  <section class="card card--front">
    <div class="brand-panel" role="img" aria-label="Decorative brand pattern in blue and grey"></div>
    <div class="details">
      <h1 class="person-name">Marcus Reid</h1>
      <p class="person-title">Manager</p>
      <ul class="contact-list">
        <li><svg viewBox="0 0 16 16"><rect x="4" y="0" width="8" height="16" rx="2"/></svg>0432 785 619</li>
        <li><svg viewBox="0 0 16 16"><path d="M3 1l3 0 1 4-2 1c1 2 3 4 5 5l1-2 4 1 0 3c0 1-1 2-2 2C7 15 1 9 1 3c0-1 1-2 2-2z"/></svg>+91 1300 987 214</li>
        <li><svg viewBox="0 0 16 16"><path d="M0 3h16v10H0z M1 4l7 5 7-5" stroke="#fff" stroke-width="1"/></svg>name@ferngatebuild.com.au</li>
        <li><svg viewBox="0 0 16 16"><circle cx="8" cy="8" r="8"/><path d="M0 8h16M8 0c-3 4-3 12 0 16M8 0c3 4 3 12 0 16" stroke="#fff" stroke-width="1" fill="none"/></svg>www.ferngatebuild.com.au</li>
      </ul>
      <p class="address">Level 3, 42 Marlow Street<br>Ashby Heights NSW 2318</p>
    </div>
  </section>

  <section class="card card--back">
    <div class="brand">
      <span class="brand-mark"></span>
      <span class="brand-name">ferngatebuild</span>
    </div>
    <p class="registration">National Provider Number 7291<br>ABN 53 219 864 317</p>
  </section>
</main>
</body>
</html>
```